Quorvane Power Point Template - Institutional Presentation

Develop a comprehensive template for a corporate presentation power point.

The presentation will be aimed to institutional investors.

Style to be modern and contemporary. Use of icons and images welcome but not to much.

It would be great if you could develop the layout/style for the content in the following slides:

- Cover
- Section title
- Slide with title and bullet points on one side and two text boxes on the other side
- Slide with line chart and pie chart
- Slide with table

Should we like the slides above we will then develop the rest of the template.

We may then need to have a dark-background version - but this will be invoiced separately.

Target Market(s)

Corporate institutional investors

Industry/Entity Type

Finance

Font styles to use
Serif
Sans Serif

Colors
3176b5
0255a3
cee9f5
86cae7
33a6d7
0792cd
33b8a4
00a990
86cfc6

Requirements
Must have
• Mostly white background with minimal objects
Nice to have
• Use of photos, but not to much.

```html
<!DOCTYPE html>
<html lang="en">
<head>
<meta charset="utf-8">
<title>Quorvane Presentation Template</title>
<link href="https://fonts.googleapis.com/css2?family=Open+Sans:wght@400;600;700&family=Montserrat:wght@600;700&display=swap" rel="stylesheet">
<style>
:root{
  --navy:#14234a;
  --blue-dark:#0255a3;
  --blue:#0d57a8;
  --blue-mid:#0792cd;
  --blue-sky:#33a6d7;
  --blue-light:#86cae7;
  --blue-pale:#cee9f5;
  --teal:#33b8a4;
  --teal-deep:#00a990;
  --teal-light:#86cfc6;
  --stage:#c4c4c4;
  --ink:#1d1d1d;
  --muted:#555;
}
*{margin:0;padding:0;box-sizing:border-box}
html,body{width:1200px;height:1169px;overflow:hidden;background:#fff}
body{position:relative;font-family:"Open Sans",Arial,sans-serif;color:var(--ink)}
.stage{position:absolute;left:0;top:0;width:1200px;height:1141px;background:var(--stage)}
.slide{position:absolute;background:#fff;overflow:hidden}
.band{position:absolute;left:0;right:0;bottom:0;display:flex}
.band span{flex:1}
.band span:nth-child(1){background:var(--blue)}
.band span:nth-child(2){background:var(--blue-sky)}
.band span:nth-child(3){background:var(--teal-deep)}
.band span:nth-child(4){background:linear-gradient(#86cfc6,#e8f6f3)}
.band-lg{height:14px}.band-sm{height:9px}

.cover-title{position:absolute;left:35px;top:68px;font-family:"Open Sans",sans-serif;font-weight:700;font-size:32px;line-height:32px;color:var(--blue-dark);letter-spacing:.2px}
.cover-project{position:absolute;left:39px;top:172px;font-size:18px;color:var(--teal)}
.cover-project b{font-weight:700}
.tag{position:absolute;background:var(--navy);color:#fff;font-family:"Montserrat",sans-serif;font-weight:600;text-align:center;letter-spacing:2px}
.tag-lg{width:104px;height:27px;line-height:27px;font-size:13px}
.tag-sm{width:62px;height:14px;line-height:14px;font-size:7px;letter-spacing:1px}

.photo{position:absolute}
.slide-title{position:absolute;font-weight:700;font-size:14px;color:#111}
.slide-title span{font-weight:400}
.slide-sub{position:absolute;font-size:7px;color:var(--muted)}
.small{font-size:5.6px;line-height:7px;color:#333}
.hl{color:var(--teal-deep);font-weight:700}
</style>
</head>
<body>
<div class="stage">

  <!-- Cover, plain -->
  <section class="slide" style="left:34px;top:72px;width:494px;height:340px">
    <h1 class="cover-title">THE FUTURE<br>OF BUSINESS<br>STARTS HERE</h1>
    <p class="cover-project"><b>Project</b> title here</p>
    <div class="tag tag-lg" style="left:34px;top:204px">QUORVANE</div>
    <div class="band band-lg"><span></span><span></span><span></span><span></span></div>
  </section>

  <!-- Cover, with image -->
  <section class="slide" style="left:626px;top:78px;width:490px;height:339px">
    <div class="photo" role="img" aria-label="Businessman holding a digital growth chart and globe" style="left:160px;top:0;width:330px;height:325px;background:radial-gradient(ellipse at 60% 55%,#9fd3e3 0%,#cfe9f0 35%,rgba(255,255,255,0) 75%),linear-gradient(90deg,#fff 0%,rgba(255,255,255,0) 30%),linear-gradient(180deg,#d9dde2,#eef6f8)"></div>
    <h1 class="cover-title" style="top:68px;left:35px">THE FUTURE<br>OF BUSINESS<br>STARTS HERE</h1>
    <p class="cover-project" style="top:170px"><b>Project</b> title here</p>
    <div class="tag tag-lg" style="left:34px;top:204px">QUORVANE</div>
    <div class="band band-lg"><span></span><span></span><span></span><span></span></div>
  </section>

  <!-- Section divider -->
  <section class="slide" style="left:10px;top:470px;width:378px;height:262px">
    <div style="position:absolute;left:0;top:0;width:180px;height:262px;background:var(--blue)"></div>
    <div class="photo" role="img" aria-label="Hands reviewing documents beside a keyboard" style="left:180px;top:0;width:198px;height:262px;background:linear-gradient(160deg,#e8eaed 0%,#c9ccd1 45%,#3a3d44 70%,#e4e6e9 100%)"></div>
    <svg style="position:absolute;left:73px;top:110px" width="40" height="36" viewBox="0 0 40 36" aria-hidden="true">
      <path d="M20 2 L38 18 H33 V34 H24 V24 H16 V34 H7 V18 H2 Z" fill="#fff"/>
      <rect x="17" y="14" width="6" height="5" fill="var(--blue)"/>
    </svg>
    <div style="position:absolute;left:44px;top:151px;color:#fff;font-size:19px">Section Title</div>
    <div style="position:absolute;left:44px;top:173px;color:#fff;font-size:7px">An Example of Subtitle here</div>
    <svg style="position:absolute;left:158px;top:162px" width="12" height="14" aria-hidden="true"><path d="M0 0 L12 7 L0 14 Z" fill="var(--teal)"/></svg>
  </section>

  <!-- Section content slide -->
  <section class="slide" style="left:405px;top:470px;width:385px;height:263px">
    <div class="slide-title" style="left:24px;top:14px">Section title <span>Here</span></div>
    <div class="slide-sub" style="left:24px;top:30px">An Example of Subtitle here</div>
    <div class="tag tag-sm" style="left:317px;top:10px">QUORVANE</div>
    <div class="photo" role="img" aria-label="Business team meeting in a bright office" style="left:32px;top:50px;width:324px;height:92px;background:linear-gradient(90deg,#5a5f66,#b7c0c7 40%,#8a9298 70%,#d5dbe0)"></div>
    <div style="position:absolute;left:32px;top:142px;width:324px;height:12px;background:var(--teal-deep);color:#fff;font-size:6.5px;line-height:12px;padding-left:12px">Title Text Here</div>
    <p class="small" style="position:absolute;left:36px;top:158px;width:150px">Our record-to-report services help you meet your goals by streamlining and consolidating operations. Using a proven method we reduce errors, raise response time and adapt quickly to changing needs. We provide reporting under local and global standards, account reconciliation, fixed asset and revenue accounting, cost and tax compliance reporting, internal control and audit support for your team.</p>
    <p class="small" style="position:absolute;left:201px;top:158px;width:150px">Streamlining and consolidating operations with a proven method lets us reduce errors, raise response time and adapt quickly to changing business needs. We provide financial reporting under local and global standards. Record-to-report services help you meet your goals, and by using a proven method we keep adapting to changing business needs.</p>
    <div class="band band-sm"><span></span><span></span><span></span><span></span></div>
  </section>

  <!-- Partners slide -->
  <section class="slide" style="left:803px;top:473px;width:387px;height:265px">
    <div class="slide-title" style="left:24px;top:16px">Sub title <span>Here</span></div>
    <div class="slide-sub" style="left:24px;top:32px">An explanation of Subtitle here</div>
    <div class="tag tag-sm" style="left:317px;top:12px">QUORVANE</div>
    <div style="position:absolute;left:21px;top:52px;width:174px;height:176px;background:#eef7fb"></div>
    <div style="position:absolute;left:199px;top:52px;width:171px;height:176px;background:#eef7fb"></div>
    <svg style="position:absolute;left:48px;top:74px" width="120" height="120" viewBox="0 0 120 120" aria-hidden="true">
      <path d="M60 0 L120 60 L60 120 L0 60 Z" fill="var(--blue)"/>
      <rect x="22" y="22" width="36" height="36" fill="var(--blue-mid)"/>
      <rect x="62" y="22" width="36" height="36" fill="var(--teal-deep)"/>
      <rect x="22" y="62" width="36" height="36" fill="var(--teal-deep)"/>
      <rect x="62" y="62" width="36" height="36" fill="var(--blue-mid)"/>
      <g fill="#fff">
        <rect x="29" y="38" width="22" height="5" rx="2.5"/>
        <rect x="70" y="42" width="3" height="9"/><rect x="75" y="36" width="3" height="15"/><rect x="80" y="32" width="3" height="19"/><rect x="85" y="28" width="3" height="23"/>
        <rect x="29" y="70" width="22" height="14" fill="none" stroke="#fff" stroke-width="2"/><rect x="38" y="84" width="3" height="7"/>
        <circle cx="74" cy="72" r="3"/><circle cx="86" cy="72" r="3"/><circle cx="80" cy="69" r="3.5"/><rect x="71" y="77" width="18" height="12" rx="3"/>
      </g>
    </svg>
    <p class="small" style="position:absolute;left:33px;top:62px;width:66px"><span class="hl" style="color:var(--blue-mid)">Insert your text:</span><br>Lorem ipsum is a simply dummy text for your printing</p>
    <p class="small" style="position:absolute;left:126px;top:62px;width:62px"><span class="hl">Insert your text:</span><br>Lorem ipsum is a simply dummy text for your printing setting</p>
    <p class="small" style="position:absolute;left:33px;top:174px;width:66px"><span class="hl">Insert your text:</span><br>Lorem ipsum is a simply dummy text for your printing setting</p>
    <p class="small" style="position:absolute;left:126px;top:174px;width:62px"><span class="hl" style="color:var(--blue-mid)">Insert your text:</span><br>Lorem ipsum is a simply dummy text for your printing setting</p>
    <div style="position:absolute;left:205px;top:65px;color:var(--teal);font-size:7px;line-height:10px">WE ARE<br>YOUR BEST</div>
    <div style="position:absolute;left:205px;top:85px;color:var(--blue-mid);font-size:13px">PARTNERS</div>
    <p class="small" style="position:absolute;left:205px;top:102px;width:78px">Corporate network so they can quickly identify and address suspicious activity on the network that could lead to risk, so they can quickly identify and address suspicious activity on the network. That could lead to so they can quickly identify and address suspicious activity</p>
    <p class="small" style="position:absolute;left:288px;top:66px;width:78px">On the network that could lead to corporate network so they identify suspicious activity on the network. That could lead to corporate network so they can quickly identify and address suspicious activity on the network so they can quickly identify and address</p>
    <div class="band band-sm"><span></span><span></span><span></span><span></span></div>
  </section>

  <!-- Line chart slide -->
  <section class="slide" style="left:10px;top:743px;width:388px;height:268px">
    <div class="slide-title" style="left:25px;top:17px">Line Chart <span>Here</span></div>
    <div class="slide-sub" style="left:25px;top:33px">An explanation of Subtitle here</div>
    <div class="tag tag-sm" style="left:319px;top:12px">QUORVANE</div>
    <svg style="position:absolute;left:0;top:0" width="388" height="230" viewBox="0 0 388 230" font-family="Open Sans, sans-serif" font-size="6">
      <text x="194" y="59" text-anchor="middle" font-weight="700" font-size="7">Chart Title</text>
      <text x="76" y="128" font-size="6" font-weight="600" transform="rotate(-90 76 128)" text-anchor="middle">Axis Title</text>
      <g fill="#333" text-anchor="end">
        <text x="102" y="71">16</text><text x="102" y="86">14</text><text x="102" y="100">12</text><text x="102" y="115">10</text><text x="102" y="129">8</text><text x="102" y="144">6</text><text x="102" y="158">4</text><text x="102" y="173">2</text><text x="102" y="187">0</text>
      </g>
      <line x1="110" y1="185" x2="318" y2="185" stroke="#999" stroke-width=".6"/>
      <polyline points="135,83.5 187,119.8 239,90.8 291,90.8" fill="none" stroke="var(--teal-deep)" stroke-width="2"/>
      <polyline points="135,127 187,141.5 239,119.8 291,148.8" fill="none" stroke="var(--blue)" stroke-width="2"/>
      <g fill="#333" font-size="5.5"><text x="138" y="86">6</text><text x="190" y="129">3</text><text x="242" y="92">4</text><text x="295" y="92">8</text><text x="138" y="130">8</text><text x="193" y="150">6</text><text x="242" y="122">9</text><text x="295" y="156">5</text></g>
      <g stroke="#999" stroke-width=".5" fill="none">
        <rect x="72" y="185" width="246" height="33"/>
        <line x1="72" y1="196" x2="318" y2="196"/><line x1="72" y1="207" x2="318" y2="207"/>
        <line x1="110" y1="185" x2="110" y2="218"/><line x1="161" y1="185" x2="161" y2="218"/><line x1="213" y1="185" x2="213" y2="218"/><line x1="265" y1="185" x2="265" y2="218"/>
      </g>
      <g fill="#333" text-anchor="middle" font-size="5.5">
        <text x="135" y="193">2000</text><text x="187" y="193">2001</text><text x="239" y="193">2002</text><text x="291" y="193">2003</text>
        <text x="135" y="204">6</text><text x="187" y="204">3</text><text x="239" y="204">4</text><text x="291" y="204">8</text>
        <text x="135" y="215">8</text><text x="187" y="215">6</text><text x="239" y="215">9</text><text x="291" y="215">5</text>
      </g>
      <line x1="75" y1="202" x2="84" y2="202" stroke="var(--teal-deep)" stroke-width="1.2"/><text x="86" y="204" font-size="5.5">Series 2</text>
      <line x1="75" y1="213" x2="84" y2="213" stroke="var(--blue)" stroke-width="1.2"/><text x="86" y="215" font-size="5.5">Series 1</text>
    </svg>
    <div class="band band-sm"><span></span><span></span><span></span><span></span></div>
  </section>

  <!-- Pie chart slide -->
  <section class="slide" style="left:410px;top:743px;width:385px;height:262px">
    <div class="slide-title" style="left:24px;top:15px">Pie Chart <span>Here</span></div>
    <div class="slide-sub" style="left:24px;top:31px">An explanation of Subtitle here</div>
    <div class="tag tag-sm" style="left:312px;top:10px">QUORVANE</div>
    <svg style="position:absolute;left:0;top:0" width="230" height="200" viewBox="0 0 230 200" font-family="Open Sans, sans-serif" font-weight="700" font-size="9" fill="#fff">
      <path d="M217,130 A90 45 0 0 1 56.9,158.2 L56.9,178.2 A90 45 0 0 0 217,150 Z" fill="#0f6fae"/>
      <path d="M56.9,158.2 A90 45 0 0 1 37,130 L37,150 A90 45 0 0 0 56.9,178.2 Z" fill="#083f7c"/>
      <path d="M127,130 L161.3,88.4 A90 45 0 1 1 56.9,158.2 Z" fill="var(--blue-mid)"/>
      <path d="M127,130 L56.9,158.2 A90 45 0 0 1 62.3,98.7 Z" fill="var(--blue-dark)"/>
      <path d="M127,130 L62.3,98.7 A90 45 0 0 1 111.4,85.7 Z" fill="var(--teal-deep)"/>
      <path d="M127,130 L111.4,85.7 A90 45 0 0 1 161.3,88.4 Z" fill="var(--teal-light)"/>
      <text x="170" y="152">58%</text><text x="46" y="128">23%</text><text x="90" y="107">10%</text><text x="120" y="104">9%</text>
    </svg>
    <div style="position:absolute;left:226px;top:90px;width:140px">
      <p class="small" style="display:flex;gap:6px;margin-bottom:8px"><b style="color:var(--blue-mid);font-size:9px;line-height:12px">59%</b><span><span style="color:var(--blue-mid)">Insert your text:</span><br>Lorem ipsum is a simply dummy text for your printing setting</span></p>
      <p class="small" style="display:flex;gap:6px;margin-bottom:8px"><b style="color:var(--blue-dark);font-size:9px;line-height:12px">23%</b><span><span style="color:var(--blue-mid)">Insert your text:</span><br>Lorem ipsum is a simply dummy text for your printing setting</span></p>
      <p class="small" style="display:flex;gap:6px;margin-bottom:8px"><b style="color:var(--teal-deep);font-size:9px;line-height:12px">10%</b><span><span style="color:var(--blue-mid)">Insert your text:</span><br>Lorem ipsum is a simply dummy text for your printing setting</span></p>
      <p class="small" style="display:flex;gap:6px"><b style="color:var(--teal-light);font-size:9px;line-height:12px">08%</b><span><span style="color:var(--blue-light)">Insert your text:</span><br>Lorem ipsum is a simply dummy text for your printing setting</span></p>
    </div>
    <div class="band band-sm"><span></span><span></span><span></span><span></span></div>
  </section>

  <!-- Table slide -->
  <section class="slide" style="left:809px;top:747px;width:381px;height:263px">
    <div class="slide-title" style="left:24px;top:17px">Pie Chart <span>Here</span></div>
    <div class="slide-sub" style="left:24px;top:33px">An explanation of Subtitle here</div>
    <div class="tag tag-sm" style="left:310px;top:12px">QUORVANE</div>
    <table class="data" style="position:absolute;left:47px;top:64px;width:301px;border-collapse:collapse;font-size:7px;text-align:center">
      <style>
        .data td,.data th{height:17.3px;border-bottom:1px solid #e3e3e3}
        .data th{font-weight:700;height:18px;font-size:6.5px}
        .data td:nth-child(1){width:86px;color:#333}
        .data td:nth-child(2){background:var(--blue-dark);color:#fff}
        .data td:nth-child(3){background:var(--blue-mid);color:#fff}
        .data td:nth-child(4){background:#5fb9e3;color:#fff}
        .data td:nth-child(5){background:var(--teal-deep);color:#fff}
        .data td:nth-child(6){background:#6fc7bb;color:#fff}
        .data td:not(:first-child){border-bottom-color:rgba(255,255,255,.25)}
      </style>
      <tr><th></th><th>2002-2004</th><th>2005-2007</th><th>2008-2010</th><th>2011-2013</th><th>2014-2016</th></tr>
      <tr><td>North America</td><td>8.9</td><td>15.6</td><td>3.3</td><td>15.6</td><td>3.3</td></tr>
      <tr><td>Latin America</td><td>11.4</td><td>11.1</td><td>8.8</td><td>11.1</td><td>8.8</td></tr>
      <tr><td>Western Europe</td><td>5.0</td><td>5.2</td><td>3.3</td><td>5.2</td><td>3.3</td></tr>
      <tr><td>Eastern Europe</td><td>14.8</td><td>17.2</td><td>10.7</td><td>17.2</td><td>10.7</td></tr>
      <tr><td>Japan</td><td>2.8</td><td>4.8</td><td>1.2</td><td>4.8</td><td>1.2</td></tr>
      <tr><td>Asia-Pacific (ex-Japan)</td><td>16.2</td><td>30.5</td><td>10.5</td><td>30.5</td><td>10.5</td></tr>
      <tr><td>Middle East and Africa</td><td>8.6</td><td>11.6</td><td>6.5</td><td>11.6</td><td>6.5</td></tr>
      <tr><td>Global</td><td>8.7</td><td>14.6</td><td>5.4</td><td>14.6</td><td>5.4</td></tr>
    </table>
    <div class="band band-sm"><span></span><span></span><span></span><span></span></div>
  </section>

</div>
</body>
</html>
```